Business Card Design

Copperfield Lantern Works, Inc. (CLW), located in Memphis, TN began operating on 2003. We are a certified
minority woman-owned business that genuinely takes a vested interest in our customers. We serve utilities,
government, contractors and end user markets in electrical, water, gas and industrial supplies. Our core
competency as a distributor of electrical materials has positioned us to serve business of all size. As your supply
chain partner, we arm you with the resources you need to make your supply chain more efficient. Our team
works with your team on a daily basis to help you solve problems and achieve goals. This team approach has
helped CLW customers to succeed and we can do the same for you.

NAICS Codes:
423610 Electrical Apparatus and Equipment, Wiring Supplies, and Related Equipment Merchant
Wholesalers
423510 Metal Service Centers and Other Metal Merchant Wholesalers
423720 Plumbing and Heating Equipment and Supplies (Hydronics) Merchant Wholesalers

Certifications
MBE (KRVPQAL, State of Kelvara Up-RFX and HJW), WBE (QOZRT),
WOSB, DOT (KVT, RLX, ZNQW, PWKT, HBRV, and TYS), LOSB,
SBE, and LSB Certified
Some of Our Products Include:
. Boxes & Covers
. Conduit & Raceway
. Fittings
. Fuses
. Lamp & Ballasts
. Lighting Controls & Timers
. Lighting Fixtures
. Personal Safety
. Pipes
. Power Distribution
. Terminations Ground & Splices
. Tools & Testers
. Wire, Cords & Cable
. Wiring Devices
. Valves

Industry/Entity Type

Business

Contact Information for Business Card

Harriet M. Pendlow - President/CEO
4817 Galvin Ave., Memphis, TN 38127
901-482-6317 office, 901-482-6319 fax, 901-358-2074 cell
hmpendlow@clwgroupx.com - www.clwworksx.com

```html
<!DOCTYPE html>
<html lang="en">
<head>
<meta charset="utf-8">
<title>Copperfield Lantern Works – Business Card</title>
<link rel="stylesheet" href="https://fonts.googleapis.com/css2?family=Marcellus&family=Marcellus+SC&family=Tinos&family=PT+Sans:ital,wght@0,400;0,700;1,400&display=swap">
<style>
  :root {
    --backdrop: #8c8c8c;
    --paper: #f4f4f4;
    --ink: #161616;
    --ink-soft: #3a3a3a;
    --olive: #9c9b16;
    --olive-line: #b4b33a;
    --reverse-text: #ffffff;
  }
  * { margin: 0; padding: 0; box-sizing: border-box; }
  html, body {
    width: 1105px; height: 1200px; overflow: hidden;
    background: var(--backdrop);
  }
  .canvas { position: relative; width: 1105px; height: 1200px; }

  .card {
    position: absolute; left: 180px; width: 745px; height: 425px;
    box-shadow: 0 6px 14px rgba(0,0,0,.28);
    overflow: hidden;
  }
  .card--front { top: 120px; background: var(--paper); }
  .card--back  { top: 640px; background: var(--olive); }

  /* front */
  .brand {
    position: absolute; right: 34px; top: 52px; text-align: right;
    font-family: "Marcellus", serif; font-size: 38px; line-height: 1.08;
    color: var(--ink); letter-spacing: .5px;
  }
  .name-bar { position: absolute; left: 0; top: 204px; width: 13px; height: 50px; background: var(--ink); }
  .person-name {
    position: absolute; left: 38px; top: 196px;
    font-family: "Marcellus SC", serif; font-weight: 400; font-size: 30px; color: var(--ink);
  }
  .person-title {
    position: absolute; left: 38px; top: 232px;
    font-family: "Marcellus SC", serif; font-size: 22px; letter-spacing: .6px; color: var(--olive);
  }
  .title-rule { position: absolute; left: 216px; right: 34px; top: 254px; height: 1px; background: var(--olive-line); }

  .contacts { position: absolute; left: 38px; top: 276px; list-style: none;
    font-family: "Tinos", serif; font-size: 22px; color: var(--ink-soft); }
  .contacts li { display: flex; align-items: center; height: 28.5px; }
  .contacts svg { width: 19px; height: 19px; margin-right: 9px; fill: var(--ink); }

  .address { position: absolute; right: 34px; top: 300px; text-align: right;
    font-family: "Tinos", serif; font-size: 22px; line-height: 28.5px; color: var(--ink-soft); }
  .address .web { color: var(--ink); }
  .footer-band { position: absolute; left: 0; bottom: 0; width: 745px; height: 14px; }

  /* back */
  .back-info { position: absolute; right: 23px; top: 22px; text-align: right;
    font-family: "PT Sans", sans-serif; color: var(--reverse-text); white-space: nowrap; }
  .back-info h2 { font-size: 23px; font-weight: 700; line-height: 27px; }
  .back-info p { font-size: 17.5px; line-height: 22.6px; }
  .back-info .section { margin-bottom: 3px; }
  .products p { font-style: italic; line-height: 23.2px; }
</style>
</head>
<body>
<div class="canvas">

  <section class="card card--front">
    <div class="brand">COPPERFIELD<br>LANTERN WORKS</div>

    <div class="name-bar"></div>
    <h1 class="person-name">Harriet M. Pendlow</h1>
    <div class="person-title">President/CEO</div>
    <div class="title-rule"></div>

    <ul class="contacts">
      <li><svg viewBox="0 0 24 24"><path d="M6.6 10.8a15.1 15.1 0 0 0 6.6 6.6l2.2-2.2c.3-.3.7-.4 1-.2 1.1.4 2.3.6 3.6.6.6 0 1 .4 1 1V20c0 .6-.4 1-1 1A17 17 0 0 1 3 4c0-.6.4-1 1-1h3.5c.6 0 1 .4 1 1 0 1.3.2 2.5.6 3.6.1.3 0 .7-.2 1z"/></svg>901-482-6317</li>
      <li><svg viewBox="0 0 24 24"><path d="M7 2h10a1.5 1.5 0 0 1 1.5 1.5v17A1.5 1.5 0 0 1 17 22H7a1.5 1.5 0 0 1-1.5-1.5v-17A1.5 1.5 0 0 1 7 2zm.8 2.5v13h8.4v-13zM12 18.6a1.1 1.1 0 1 0 0 2.2 1.1 1.1 0 0 0 0-2.2z"/></svg>901-482-6319</li>
      <li><svg viewBox="0 0 24 24"><path d="M6 2h9l3 3v4H6zM3 10h18a1 1 0 0 1 1 1v8a1 1 0 0 1-1 1H3a1 1 0 0 1-1-1v-8a1 1 0 0 1 1-1zm3 5v2h12v-2z"/></svg>901-358-2074</li>
      <li><svg viewBox="0 0 24 24"><path d="M2 5h20v14H2zm2 2v.4l8 5.2 8-5.2V7zm0 2.8V17h16V9.8l-8 5.2z"/></svg>hmpendlow@clwgroupx.com</li>
    </ul>

    <div class="address">
      4817 Galvin Ave.<br>
      Memphis, TN 38127<br>
      <span class="web">www.clwworksx.com</span>
    </div>

    <svg class="footer-band" viewBox="0 0 745 14" preserveAspectRatio="none">
      <polygon points="0,0 491,0 486,14 0,14" fill="var(--ink)"/>
      <polygon points="496,0 745,0 745,14 491,14" fill="var(--olive)"/>
    </svg>
  </section>

  <section class="card card--back">
    <div class="back-info">
      <div class="section">
        <h2>NAICS Codes:</h2>
        <p>423610 Electrical Apparatus &amp; Equipment</p>
        <p>Wiring Supplies, &amp; Related Equipment Merchant, Wholesalers</p>
        <p>423510 Metal Service Centers &amp; Other Metal Merchant Wholesalers</p>
        <p>423720 Plumbing &amp; Heating Equipment &amp; Supplies (Hydronics)</p>
        <p>Merchant Wholesalers</p>
      </div>
      <div class="section">
        <h2>Certifications</h2>
        <p>MBE (KRVPQAL, State of Kelvara Up-RFX and HJW), WBE (QOZRT)</p>
        <p>WOSB, DOT (KVT, RLX, ZNQW, PWKT, HBRV, and TYS), LOSB</p>
        <p>SBE, &amp; LSB Certified</p>
      </div>
      <div class="section products">
        <h2>Some of Our Products Include:</h2>
        <p>Boxes &amp; Covers | Conduit &amp; Raceway | Fittings</p>
        <p>Fuses | Lamp &amp; Ballasts | Lighting Controls &amp; Timers | Lighting Fixtures</p>
        <p>Personal Safety | Pipes | Power Distribution | Tools &amp; Testers</p>
        <p>Wire, Cords &amp; Cable | Terminations Ground &amp; Splices</p>
        <p>Wiring Devices | Valves</p>
      </div>
    </div>
  </section>

</div>
</body>
</html>
```